Re-design association of teachers webplattform

I need a complete re-design for an existing association of teachers website. I will create it in wordpress in the next months.

It should be modern, but more an information plattform for teachers in our region (Switzerland, south -> near the alps).
Following content are contained:
- blog
- calendar
- text only
- document only (a list of documents to download -> pdf)
- social media
- login area

What I need is :
- a well color concept
- an inspiration how to use images (or without images)
- an inspiration where to place logo (attached file) / text / navigation

```html
<!DOCTYPE html>
<html lang="de">
<head>
<meta charset="utf-8">
<title>lehrnetz – Verein der Lehrpersonen</title>
<link href="https://fonts.googleapis.com/css2?family=Lexend:wght@400;500&family=Roboto:wght@400;500;700&family=Roboto+Condensed:wght@400;700&display=swap" rel="stylesheet">
<style>
:root{
  --blue:#0a8fd1;
  --blue-deep:#0077b6;
  --green:#c8d95a;
  --green-text:#7ba21c;
  --cream:#fdfdf0;
  --ink:#333;
  --white:#fff;
}
*{box-sizing:border-box;margin:0;padding:0}
html,body{width:1200px;height:4491px;overflow:hidden}
body{position:relative;background:var(--cream);font-family:Roboto,sans-serif;color:var(--ink)}
.abs{position:absolute}
.heading{font-family:Lexend,sans-serif;font-weight:400}
.nav a,.foot-nav a{font-family:"Roboto Condensed",sans-serif;font-weight:700;font-size:13px;color:#333;text-decoration:none;position:absolute}
.brand{font-family:Lexend,sans-serif;font-weight:500;color:var(--blue);display:flex;align-items:center;gap:8px}
.brand .dot{width:22px;height:22px;border-radius:50%;background:var(--green)}
.para{font-size:13.5px;line-height:20px}
.pill{position:absolute;border-radius:30px;color:#fff;font-size:14px;display:flex;align-items:center;justify-content:center}
.photo{position:absolute;overflow:hidden}
/* calendar */
.events{background:var(--blue);border:2px solid #fff}
.event{position:absolute;left:30px;width:230px}
.event .date{font-size:11.5px;font-weight:700;color:#fff}
.event .title{font-family:Lexend,sans-serif;font-size:15.5px;color:#e6ef8a;margin-top:10px;line-height:19px}
.cal{background:#fff;border:2px solid #ddd}
.cal span{position:absolute;width:60px;margin-left:-30px;text-align:center;font-size:13px;color:#888}
.cal .dow{font-size:10.5px;font-weight:700;color:#333}
.cal .strong{color:#222}
.cal i{position:absolute;width:4px;height:4px;border-radius:50%;top:20px;left:28px}
/* blog */
.card{position:absolute;width:298px;height:420px;background:#fff;border:1px solid #ccc;overflow:hidden}
.card .img{height:200px}
.card h3{font-family:Lexend,sans-serif;font-weight:400;color:var(--blue);font-size:20px;line-height:24px;margin:40px 26px 0}
.card p{font-size:11.5px;line-height:15px;color:#888;margin:18px 26px 0}
.card .date{position:absolute;left:26px;bottom:-12px;width:152px;height:50px;border-radius:80px 80px 0 0;background:var(--green);color:#fff;font-size:13px;text-align:center;padding-top:14px}
.social i{position:absolute;width:44px;height:44px;border-radius:50%;background:var(--blue)}
</style>
</head>
<body>

<!-- Header -->
<header class="abs" style="left:0;top:0;width:1200px;height:107px;background:#fff">
  <div class="brand abs" style="left:150px;top:28px;font-size:40px">lehrnetz<span class="dot"></span></div>
  <div class="abs" style="left:762px;top:0;width:190px;height:36px;background:var(--blue);border-radius:0 0 20px 20px"></div>
  <div class="abs" style="left:800px;top:10px;display:flex;gap:16px">
    <span style="width:14px;height:14px;border-radius:50%;background:#fff"></span>
    <span style="width:14px;height:14px;border-radius:50%;background:#fff"></span>
    <span style="width:14px;height:14px;border-radius:50%;background:#fff"></span>
    <span style="width:14px;height:14px;border-radius:50%;background:#fff"></span>
  </div>
  <div class="abs" style="left:958px;top:0;width:92px;height:36px;background:var(--green);border-radius:0 0 20px 20px;color:#fff;font-family:'Roboto Condensed',sans-serif;font-weight:700;font-size:14px;text-align:center;line-height:34px">LOGIN</div>
  <nav class="nav">
    <a style="left:510px;top:70px;color:var(--green-text)">HOME</a>
    <a style="left:585px;top:70px">ABOUT</a>
    <a style="left:672px;top:70px">WHAT WE DO</a>
    <a style="left:798px;top:70px">BLOG</a>
    <a style="left:876px;top:70px">CALENDAR</a>
    <a style="left:988px;top:70px">CONTACT</a>
  </nav>
</header>

<!-- Hero -->
<section class="abs" style="left:0;top:107px;width:1200px;height:620px">
  <div class="photo" role="img" aria-label="Smiling teacher in a classroom with pupils at a chalkboard" style="left:0;top:0;width:1200px;height:620px;background:linear-gradient(90deg,#9a7a5e 0%,#7d8c78 35%,#c9b9a6 60%,#e5a88d 80%,#a89784 100%)"></div>
  <svg class="abs" style="left:0;top:0" width="1200" height="620" viewBox="0 0 1200 620">
    <path d="M0 460 C300 600 520 630 760 560 C950 505 1080 470 1200 455 L1200 620 L0 620 Z" fill="var(--blue)"/>
    <path d="M0 490 C300 620 520 650 760 585 C950 530 1080 500 1200 495 L1200 620 L0 620 Z" fill="var(--cream)"/>
  </svg>
  <div class="abs" style="left:110px;top:148px;width:488px;height:211px;background:rgba(16,150,215,.88);color:#fff;padding:26px 34px">
    <div class="heading" style="font-size:28px;line-height:34px">Verein der Lehrpersonen an der Bergtaler Sekundarschule</div>
    <div class="heading" style="font-size:36px;margin-top:14px;padding-left:6px">Sektion Hochtal</div>
  </div>
</section>

<!-- Welcome -->
<h1 class="heading abs" style="left:0;top:790px;width:1200px;text-align:center;font-size:58px;color:var(--green-text)">Welcome to lehrnetz</h1>
<p class="para abs" style="left:195px;top:874px;width:810px;text-align:center">Lorem ipsum dolor sit amet, consectetur adipiscing elit, sed do eiusmod tempor incididunt ut labore et dolore magna aliqua. Quis ipsum suspendisse ultrices gravida. Risus commodo viverra maecenas accumsan lacus vel facilisis. Lorem ipsum dolor sit amet, consectetur adipiscing elit, sed do eiusmod tempor incididunt ut labore et dolore magna aliqua. Quis ipsum suspendisse ultrices gravida. Risus commodo viverra maecenas accumsan lacus vel facilisis.</p>

<!-- Feature 1 -->
<svg class="abs" style="left:0;top:1060px" width="1200" height="520" viewBox="0 0 1200 520">
  <path d="M0 340 C120 420 280 420 420 400 C560 380 650 360 700 350 L700 520 L0 520 Z" fill="var(--cream)"/>
  <path d="M0 335 C140 430 300 420 440 395 C560 375 640 360 700 350 L700 370 C620 385 540 400 440 420 C300 445 130 445 0 380 Z" fill="var(--green)"/>
  <circle cx="870" cy="240" r="208" fill="var(--green)"/>
  <circle cx="863" cy="264" r="206" fill="var(--blue)"/>
  <circle cx="863" cy="250" r="198" fill="#fff"/>
</svg>
<div class="photo" role="img" aria-label="Teacher in a yellow cardigan pointing at a chalkboard" style="left:665px;top:1112px;width:400px;height:400px;border-radius:50%;background:radial-gradient(circle at 40% 45%,#d8b24a 0%,#5c5f5e 45%,#3a3d3d 100%)"></div>
<h2 class="heading abs" style="left:148px;top:1095px;font-size:56px;color:var(--blue)">Lorem susalise</h2>
<p class="para abs" style="left:148px;top:1173px;width:470px">Lorem ipsum dolor sit amet, consectetur adipiscing elit, sed do eius mod tempor incididunt ut labore et dolore magna aliqua. Quis ipsum suspendisse ultrices gravida. Risus commodo viverra maecenas accumsan lacus vel facilisis. Lorem ipsum dolor sit amet, consectetur adipiscing elit, sed do eiusmod tempor incididunt ut.</p>
<div class="pill" style="left:144px;top:1297px;width:137px;height:40px;background:var(--blue)">READ MORE</div>

<!-- Feature 2 -->
<div class="abs" style="left:0;top:1480px;width:1200px;height:700px;background:#fff"></div>
<svg class="abs" style="left:60px;top:1690px" width="520" height="510" viewBox="0 0 520 510">
  <circle cx="254" cy="242" r="240" fill="var(--green)"/>
  <circle cx="254" cy="230" r="236" fill="#fff"/>
</svg>
<div class="photo" role="img" aria-label="Smiling male teacher with a clipboard in a classroom" style="left:92px;top:1705px;width:444px;height:444px;border-radius:50%;background:radial-gradient(circle at 45% 50%,#6f7fa3 0%,#c9c4bd 50%,#e8e6e3 100%)"></div>
<h2 class="heading abs" style="left:586px;top:1707px;font-size:56px;color:var(--green)">Lorem susalise</h2>
<p class="para abs" style="left:586px;top:1785px;width:470px">Lorem ipsum dolor sit amet, consectetur adipiscing elit, sed do eius mod tempor incididunt ut labore et dolore magna aliqua. Quis ipsum suspendisse ultrices gravida. Risus commodo viverra maecenas accumsan lacus vel facilisis. Lorem ipsum dolor sit amet, consectetur adipiscing elit, sed do eiusmod tempor incididunt ut.</p>
<div class="pill" style="left:582px;top:1909px;width:137px;height:40px;background:var(--green)">READ MORE</div>

<!-- Calendar -->
<svg class="abs" style="left:0;top:2160px" width="1200" height="920" viewBox="0 0 1200 920">
  <path d="M0 40 C200 20 450 -10 650 10 C900 35 1050 25 1200 0 L1200 780 C1050 800 950 820 700 830 C450 840 250 780 0 790 Z" fill="var(--green)"/>
  <path d="M0 70 C200 40 450 5 650 15 C900 30 1050 40 1200 25 L1200 755 C1050 770 950 790 700 800 C450 810 200 740 0 760 Z" fill="var(--blue)"/>
  <path d="M0 760 C150 740 300 760 450 800 C550 825 650 850 760 840 C900 828 1050 780 1200 770 L1200 920 L0 920 Z" fill="var(--cream)"/>
  <path d="M0 770 C130 760 280 795 430 835 C530 860 640 880 760 868 C900 855 1050 800 1200 790 L1200 920 L0 920 Z" fill="#fff"/>
</svg>
<h2 class="heading abs" style="left:0;top:2282px;width:1200px;text-align:center;font-size:56px;color:#fff">Our Calendar</h2>
<div class="events abs" style="left:152px;top:2412px;width:281px;height:406px">
  <div class="event" style="top:26px"><div class="date">Apr 06 2022</div><div class="title">Lorem ipsum dolor sit ame cons lorem ispectetur</div></div>
  <div class="event" style="top:120px"><div class="date">Apr 06 2022</div><div class="title">Lorem ipsum dolor sit ame consect lorem ispetur</div></div>
  <div class="event" style="top:210px"><div class="date">Apr 06 2022</div><div class="title">Lorem ilorempsum dolor sit amelo con sectetur</div></div>
  <div class="event" style="top:314px"><div class="date">Apr 06 2022</div><div class="title">Lorem ipsum dolor sit ame cons loremectetur</div></div>
</div>
<div class="cal abs" style="left:476px;top:2407px;width:592px;height:410px">
  <div class="abs" style="left:38px;top:24px;font-size:19px;color:#333">February 2015 ›</div>
  <div class="abs" style="left:494px;top:32px;font-size:9px;color:var(--green-text)">⊕ Add Event</div>
  <span class="dow" style="left:53px;top:88px">SUN</span><span class="dow" style="left:134px;top:88px">MON</span><span class="dow" style="left:217px;top:88px">TUE</span><span class="dow" style="left:299px;top:88px">WED</span><span class="dow" style="left:380px;top:88px">THU</span><span class="dow" style="left:462px;top:88px">FRI</span><span class="dow" style="left:544px;top:88px">SAT</span>
  <span style="left:53px;top:142px">1</span><span style="left:134px;top:142px">2</span><span style="left:217px;top:142px">3</span><span style="left:299px;top:142px">4<i style="background:#5ab55a"></i></span><span style="left:380px;top:142px">5</span><span style="left:462px;top:142px">6</span><span style="left:544px;top:142px">7</span>
  <span style="left:53px;top:198px">8</span><span style="left:134px;top:198px">9</span><span style="left:217px;top:198px">10</span><span style="left:299px;top:198px">11</span><span style="left:380px;top:198px">12</span><span style="left:462px;top:198px">13</span><span style="left:544px;top:198px">14</span>
  <span style="left:53px;top:255px">15<i style="background:var(--blue)"></i></span><span style="left:134px;top:255px">16</span><span style="left:217px;top:255px">17<i style="background:#e8743b"></i></span><span class="strong" style="left:299px;top:255px">18</span><span class="strong" style="left:380px;top:255px">19<i style="background:var(--blue);left:25px"></i><i style="background:#e8743b;left:31px"></i></span><span class="strong" style="left:462px;top:255px">20</span><span class="strong" style="left:544px;top:255px">21</span>
  <span class="strong" style="left:53px;top:311px">22</span><span class="strong" style="left:134px;top:311px">23<i style="background:#5ab55a"></i></span><span class="strong" style="left:217px;top:311px">24</span><span class="strong" style="left:299px;top:311px">25</span><span class="strong" style="left:380px;top:311px">26</span><span class="strong" style="left:462px;top:311px">27</span><span class="strong" style="left:544px;top:311px">28<i style="background:#5ab55a"></i></span>
</div>

<!-- Blog -->
<div class="abs" style="left:0;top:3060px;width:1200px;height:740px;background:#fff"></div>
<h2 class="heading abs" style="left:0;top:3160px;width:1200px;text-align:center;font-size:56px;color:var(--blue)">Latest Blog</h2>
<article class="card" style="left:126px;top:3265px">
  <div class="img" role="img" aria-label="Teacher with a tablet in front of a classroom" style="background:linear-gradient(135deg,#c85a4a,#d9cfc4 60%,#8aa0b8)"></div>
  <h3>Lorem ipsum dolor sit amet, consectetur</h3>
  <p>Lorem ipsum dolor sit amet, consec tetur adipiscing elit, sed do eiusm od tempor incididunt ut labore et dolore magna aliqua.</p>
  <div class="date">Apr 05 2022</div>
</article>
<article class="card" style="left:444px;top:3265px">
  <div class="img" role="img" aria-label="Teacher writing on a whiteboard" style="background:linear-gradient(135deg,#e5e4e1,#c9a598 55%,#6b4e3a)"></div>
  <h3>Lorem ipsum dolor sit amet, consectetur</h3>
  <p>Lorem ipsum dolor sit amet, consec tetur adipiscing elit, sed do eiusm od tempor incididunt ut labore et dolore magna aliqua.</p>
  <div class="date">Apr 05 2022</div>
</article>
<article class="card" style="left:771px;top:3265px">
  <div class="img" role="img" aria-label="Teacher with pupils raising hands" style="background:linear-gradient(135deg,#d88a8a,#e8d2b8 50%,#6f93c4)"></div>
  <h3>Lorem ipsum dolor sit amet, consectetur</h3>
  <p>Lorem ipsum dolor sit amet, consec tetur adipiscing elit, sed do eiusm od tempor incididunt ut labore et dolore magna aliqua.</p>
  <div class="date">Apr 05 2022</div>
</article>

<!-- Download CTA -->
<svg class="abs" style="left:0;top:3780px" width="1200" height="380" viewBox="0 0 1200 380">
  <path d="M0 170 C150 110 300 20 520 10 C750 0 1000 60 1200 150 L1200 380 L0 380 Z" fill="var(--blue)"/>
  <path d="M0 195 C150 140 300 50 520 40 C750 30 1000 90 1200 180 L1200 380 L0 380 Z" fill="var(--green)"/>
</svg>
<p class="heading abs" style="left:152px;top:3990px;width:580px;font-size:30px;line-height:34px;color:#fff">Lorem ipsum dolor sit amet, consectetur adipiscing elit, sed do eiusmod tempor incididunt ut labore et dolore</p>
<div class="pill heading" style="left:759px;top:4010px;width:291px;height:65px;background:var(--blue);font-size:30px;border:2px solid #fff;gap:10px">
  <svg width="20" height="26" viewBox="0 0 20 26"><path d="M0 0 H13 L20 7 V26 H0 Z" fill="#fff"/><path d="M13 0 V7 H20" fill="#cfe6f5"/></svg>Download PDF
</div>

<!-- Footer -->
<footer class="abs" style="left:0;top:4157px;width:1200px;height:334px;background:#fff">
  <div class="abs" style="left:190px;top:78px;font-family:'Roboto Condensed',sans-serif;font-weight:700;font-size:20px;color:var(--green)">CALL US: 0800 555 01 23</div>
  <div class="abs" style="left:784px;top:78px;font-family:'Roboto Condensed',sans-serif;font-weight:700;font-size:20px;color:var(--green)">Email:info@lehrnetz.example</div>
  <div class="brand abs" style="left:468px;top:92px;font-size:50px">lehrnetz<span class="dot" style="width:30px;height:30px"></span></div>
  <nav class="foot-nav">
    <a style="left:190px;top:138px">HOME</a>
    <a style="left:264px;top:138px">ABOUT</a>
    <a style="left:352px;top:138px">WHAT WE DO</a>
    <a style="left:758px;top:138px">BLOG</a>
    <a style="left:836px;top:138px">CALENDAR</a>
    <a style="left:948px;top:138px">CONTACT</a>
  </nav>
  <div class="abs" style="left:0;top:196px;width:1200px;height:3px;background:var(--blue)"></div>
  <div class="abs" style="left:0;top:226px;width:1200px;text-align:center;font-size:17px;color:#333">© 2022 All Rights Reserved. Privacy Policy Terms and Conditions</div>
  <div class="social">
    <i style="left:473px;top:271px"></i><i style="left:541px;top:271px"></i><i style="left:611px;top:271px"></i><i style="left:681px;top:271px"></i>
  </div>
</footer>

</body>
</html>
```